Start up in business consultancy needs a business card

We need the business card's layout (we have already the logo). Our business is concerned on consultancy services delivered to companies on the matter of sustainability. Business card should be enough essentials and professional style.

Side A with the following info:
logo + a space for the claim (still to identify) + website of the company

Side B with the following info:
Name of business card holder + title of the business card holder + address of the company + space for mobile number, phone number, fax number + e-mail of business card holder + graphic details around.

Target Market(s)

Business of any sector

Industry/Entity Type

Business Service

Contact Information for Business Card

Name of the company:
Pianoverde srl
Società Benefit

Address of the company:
Via Lucerna, 7
21047 - Saronno (VA)

Website:
www.pianoverde.it

Name of the BC' holder:
Luca Ferentino

Title:
Co-fondatore

Email:
luca@pianoverde.it

Mobile:
+39 348 915 2074
Phone:
+39 348 915 2074
Fax:
+39 348 915 2074

Font styles to use
Other font styles liked:
• new gothic

```html
<!DOCTYPE html>
<html lang="it">
<head>
<meta charset="utf-8">
<title>Pianoverde srl – Biglietto da visita</title>
<link rel="stylesheet" href="https://fonts.googleapis.com/css2?family=Source+Sans+3:wght@400;600;700&display=swap">
<style>
  :root {
    --backdrop: #2f2a27;
    --paper: #f7f7f5;
    --brand-blue: #1f65ad;
    --card-blue: #0d67ad;
    --ink: #3a3a3a;
    --white: #ffffff;
    --ring-faint: rgba(255,255,255,0.14);
  }
  * { box-sizing: border-box; margin: 0; padding: 0; }
  html, body {
    width: 1200px; height: 844px; overflow: hidden;
    background: var(--backdrop);
    font-family: "Source Sans 3", "Myriad Pro", sans-serif;
  }
  .stage {
    position: relative; width: 1200px; height: 844px;
    display: flex; align-items: center; justify-content: center; gap: 50px;
  }
  .card {
    position: relative; width: 520px; height: 330px;
    box-shadow: 0 10px 24px rgba(0,0,0,0.45);
    overflow: hidden;
  }

  /* Front side: contact details */
  .card--contact { background: var(--paper); color: var(--ink); }
  .brand {
    position: absolute; top: 50px; left: 0; right: 0;
    display: flex; align-items: center; justify-content: center; gap: 16px;
  }
  .brand__dot {
    width: 64px; height: 64px; border-radius: 50%;
    border: 4px solid var(--brand-blue);
  }
  .brand__name {
    font-size: 44px; font-weight: 600; color: var(--brand-blue);
    letter-spacing: -0.5px;
  }
  .holder {
    position: absolute; left: 40px; top: 175px;
  }
  .holder__name { font-size: 20px; font-weight: 700; color: var(--brand-blue); }
  .holder__title { font-size: 15px; margin-top: 2px; }
  .address { position: absolute; left: 40px; top: 236px; font-size: 15px; }
  .website--front {
    position: absolute; right: 34px; top: 178px;
    font-size: 14px; font-weight: 700; color: var(--brand-blue);
  }
  .contacts {
    position: absolute; left: 40px; top: 270px;
    display: grid; grid-template-columns: auto auto; column-gap: 26px; row-gap: 4px;
    font-size: 15px;
  }
  .contacts__item { white-space: nowrap; }
  .contacts__label { color: var(--brand-blue); font-weight: 700; margin-right: 6px; }

  /* Back side: benefits */
  .card--benefits { background: var(--card-blue); color: var(--white); text-align: center; }
  .benefits { position: absolute; top: 42px; left: 0; right: 0; }
  .benefits__heading { font-size: 19px; font-weight: 700; letter-spacing: 0.2px; margin-bottom: 10px; }
  .benefits__list { list-style: none; font-size: 17px; line-height: 25px; }
  .website--back { position: absolute; bottom: 70px; left: 0; right: 0; font-size: 13px; font-weight: 700; }
</style>
</head>
<body>
<main class="stage">
  <section class="card card--contact" aria-label="Fronte del biglietto">
    <div class="brand">
      <span class="brand__dot" aria-hidden="true"></span>
      <span class="brand__name">pianoverde</span>
    </div>
    <div class="holder">
      <p class="holder__name">Luca Ferentino</p>
      <p class="holder__title">Co-fondatore</p>
    </div>
    <p class="address">Via Lucerna, 7 21047 - Saronno (VA)</p>
    <p class="website--front">www.pianoverde.it</p>
    <div class="contacts">
      <p class="contacts__item"><span class="contacts__label">M:</span>+39 348 915 2074</p>
      <p class="contacts__item"><span class="contacts__label">P:</span>+39 348 915 2074</p>
      <p class="contacts__item"><span class="contacts__label">F:</span>+39 348 915 2074</p>
      <p class="contacts__item"><span class="contacts__label">E:</span>luca@pianoverde.it</p>
    </div>
  </section>

  <section class="card card--benefits" aria-label="Retro del biglietto">
    <div class="benefits">
      <h2 class="benefits__heading">COMPANY BENEFITS</h2>
      <ul class="benefits__list">
        <li>Benfit point One</li>
        <li>Benfit point Number Two</li>
        <li>Benfit point Three</li>
        <li>Benfit point Number Four</li>
        <li>Benfit point Five</li>
      </ul>
    </div>
    <p class="website--back">www.pianoverde.it</p>
  </section>
</main>
</body>
</html>
```